Vantor Health Group Presentation Folder, for Cancer Awareness, VERY COLORFUL AND MODERN

Presentation Folder I know pretty much what i want so it should be very eazy , I have included files from folders I use now rebrand them to my new company they will be fine, no sense re creating the wheel
Full Bleed Size
20.87" x 16.68"
53 x 42.4 cm
6260 x 5004 pixels
Document Trim Size
20.75" x 16.56"
52.7 x 42.1 cm
6225 x 4969 pixels
Updates

Low design quality

Industry/Entity Type

Medical

Font styles to use
Serif

Colors

Designer to choose colors to be used in the design.

Requirements
Must have
• really I am not looking for some one to redesign, we like our folder front page and would like to see new word information added., there are two folder front pages to choose from
• So Keep the original front page and redesign the back page and the pockets
• Can Make your Design off of one of the ones I already uploaded
Nice to have
• Keep the same color schemes, Keep the original front page and redesign the back page and the pockets
Should not have
• DO not recreate the front covers, use what I gave you and just rebrand

```html
<!DOCTYPE html>
<html lang="en">
<head>
<meta charset="utf-8">
<title>Vantor Health Group – Presentation Folder</title>
<link href="https://fonts.googleapis.com/css2?family=Raleway:wght@300;400;500;700;800&display=swap" rel="stylesheet">
<style>
  :root{
    --stage:#5f5f5f;
    --paper:#ffffff;
    --cut:#e0433a;
    --fold:#3fbf6a;
    --guide:#6cc6ee;
    --pink:#ee8aa6;
    --navy:#1d2a6b;
    --green:#8dc63f;
    --green-text:#79b72c;
    --band:#7b7b7b;
    --ink:#3a3a3a;
    --ribbon-area:#d7a6e2;
  }
  *{box-sizing:border-box;margin:0;padding:0}
  html,body{width:1200px;height:1000px;overflow:hidden}
  body{background:var(--stage);font-family:"Raleway",sans-serif;color:var(--ink);position:relative}
  .dieline{position:absolute;inset:0}
  .guide-frame{position:absolute;border:1px solid var(--guide)}
  .photo{position:absolute;box-shadow:0 6px 14px rgba(0,0,0,.25)}
  .photo--beach{left:124px;top:178px;width:426px;height:280px;transform:rotate(-4deg);
    background:linear-gradient(160deg,#3a8ce4 0%,#8fc2ee 100%)}
  .photo--table{left:656px;top:286px;width:418px;height:270px;transform:rotate(-4deg);
    background:linear-gradient(160deg,#ece8e0 0%,#c9b9a0 100%)}
  .ribbon-area{position:absolute;width:40px;height:72px;background:var(--ribbon-area)}
  .ribbon-area--left{left:494px;top:118px}
  .ribbon-area--right{left:1022px;top:214px}
  .intro{position:absolute;left:126px;top:517px;width:430px;font-size:10.2px;line-height:12.4px;color:#333}
  .intro strong{color:var(--green-text);font-weight:700}
  .intro p{margin-bottom:13px}
  .intro .callout{color:var(--navy);font-size:11.4px;line-height:13.4px;font-weight:500}
  .title{position:absolute;left:666px;top:116px;font-size:23px;letter-spacing:1.6px;color:var(--pink);font-weight:500;white-space:nowrap}
  .subtitle{position:absolute;left:618px;top:152px;width:520px;text-align:center;font-size:14px;font-weight:500;color:#222}
  .lede{position:absolute;left:672px;top:182px;width:412px;text-align:center;font-size:11.4px;line-height:14px;color:#444}
  .band{position:absolute;left:600px;top:598px;width:496px;height:36px;background:var(--band)}
  .band__text{position:absolute;left:142px;top:8px;font-size:16px;font-weight:300;color:#fff;white-space:nowrap}
  .band__mark{position:absolute;left:76px;top:12px;width:44px;height:44px;border-radius:50%;background:#fff;border:3px solid var(--navy)}
  .flip{transform:rotate(180deg)}
  .pocket-left-content{position:absolute;left:124px;top:720px;width:436px;height:200px}
  .lockup{position:absolute;left:160px;top:78px;display:flex;align-items:center;gap:7px}
  .lockup__dot{width:26px;height:26px;border-radius:50%;background:var(--navy);flex:none}
  .lockup__name{font-size:11px;line-height:12px;font-weight:800;color:var(--navy)}
  .company{position:absolute;left:100px;top:156px;font-size:13px;font-weight:800;color:var(--navy)}
  .division{position:absolute;left:100px;top:175px;font-size:11.6px;color:#222}
  .pocket-right-content{position:absolute;left:634px;top:720px;width:430px;height:200px;padding:26px 0 0 24px}
  .fine{width:350px;font-size:6.2px;line-height:7.6px;color:#222;margin-bottom:6px}
  .pocket-heading{font-size:14.6px;line-height:18.6px;font-weight:800;color:var(--navy);margin-top:10px;white-space:nowrap}
</style>
</head>
<body>
  <svg class="dieline" width="1200" height="1000" viewBox="0 0 1200 1000" aria-hidden="true">
    <path d="M48,60 H1156 V445 A17,17 0 0 0 1156,479 V700 H48 V479 A17,17 0 0 0 48,445 Z" fill="var(--paper)" stroke="var(--cut)" stroke-width="1"/>
    <path d="M90,700 H596 L586,918 Q582,942 556,942 H90 Z" fill="var(--paper)" stroke="var(--cut)" stroke-width="1"/>
    <path d="M604,700 H1112 V942 H650 Q624,942 620,918 Z" fill="var(--green)" stroke="var(--cut)" stroke-width="1"/>
    <path d="M126,720 H562 L556,902 Q552,922 530,922 H126 Z" fill="none" stroke="var(--guide)" stroke-width="1"/>
    <path d="M630,720 H1066 V922 H668 Q648,922 644,902 Z" fill="none" stroke="var(--guide)" stroke-width="1"/>
    <line x1="600" y1="60" x2="600" y2="700" stroke="var(--fold)" stroke-width="1" stroke-dasharray="3 3"/>
    <line x1="90" y1="700" x2="1112" y2="700" stroke="var(--fold)" stroke-width="1" stroke-dasharray="3 3"/>
    <g stroke="var(--cut)" stroke-width="1">
      <line x1="248" y1="804" x2="278" y2="772"/>
      <line x1="406" y1="772" x2="438" y2="804"/>
      <line x1="248" y1="852" x2="278" y2="884"/>
      <line x1="406" y1="884" x2="438" y2="852"/>
    </g>
  </svg>

  <div class="guide-frame" style="left:106px;top:76px;width:476px;height:606px"></div>
  <div class="guide-frame" style="left:618px;top:76px;width:476px;height:606px"></div>

  <div class="photo photo--beach" role="img" aria-label="Photo of a multi-generation family in white walking hand in hand along a beach"></div>
  <div class="ribbon-area ribbon-area--left" role="img" aria-label="Cancer awareness ribbon illustration"></div>

  <div class="intro">
    <p><strong>Hereditary cancer screening</strong> provides vital information to help people with a strong personal or family history of cancer understand their own risk of developing the disease. With this information, they can take steps to Potentially Prevent Cancer, Delay the Onset of Cancer or Catch it at an Earlier stage when outcomes and survival rates are Better.</p>
    <p class="callout">Don't be Afraid of the Answer: Knowledge is Power and Power Eradicates Fear. When You are Fearless, You Will Make all the Right Choices!</p>
    <p class="callout">Directions – USE any family picture I provided AND THE WORDS -Use you creativity to make it nice</p>
  </div>

  <h1 class="title">HEREDITARY CANCER SCREENING</h1>
  <p class="subtitle">Doctors are the Gatekeepers to Genetic Testing.</p>
  <p class="lede">We have an obligation to help patients understand genetic risk and how testing can guide heath care decisions.</p>
  <div class="photo photo--table" role="img" aria-label="Photo of a family of three generations sharing a meal at an outdoor table"></div>
  <div class="ribbon-area ribbon-area--right" role="img" aria-label="Cancer awareness ribbon illustration"></div>

  <div class="band">
    <div class="band__mark"></div>
    <p class="band__text">The test you order FOR your patients</p>
  </div>

  <div class="pocket-left-content flip">
    <div class="lockup"><span class="lockup__dot"></span><span class="lockup__name">VANTOR<br>HEALTH<br>GROUP</span></div>
    <p class="company">Vantor Health Group</p>
    <p class="division">a division of Meridian Clinical Sales LLC</p>
  </div>

  <div class="pocket-right-content flip">
    <p class="fine">There are many benefits to getting tested, regardless of the result. If one of your family members has had cancer, there is a chance you inherited a gene change that raises your own risk. Those who carry such a change could pass it to the next generation. The sooner testing is done, the more likely that risk can be managed well.</p>
    <p class="fine">Hereditary cancer screening provides vital information to help people with a strong personal or family history of cancer understand their own risk of developing the disease. With this information, they can take steps to Potentially Prevent Cancer, Delay the Onset of Cancer or Catch it at an Earlier stage when outcomes and survival rates are Better.</p>
    <h2 class="pocket-heading">Identifying an inherited genetic<br>mutation has the potential to prevent cancer<br>and save lives.</h2>
  </div>
</body>
</html>
```